Chartered Professional Accounting Firm Needs a Business Card Design

We need a card design for an accounting firm based in Toronto, Ontario. The firm name is Lorne Patek Professional Corporation. The owner of the firm is a chartered professional accountant and a certified general accountant. Services of the firm include 60% tax preparation and consulting and 40% financial statements for corporation year-end. We would like a modern design. The color could be black, white, gray, blue or other color to bring more confidence to clients. The logo of the firm should be included in the design. Thanks
Updates

Name: Lorne Patek, CPA, CGA Address: 47 Marrow Creek Rd. Elmbrook, ON K7T 5P3 Telephone: (416) 555-0142 Fax:(416) 555-0187 Email: lorne@lornepatek.example

Industry/Entity Type

Accounting

```html
<!DOCTYPE html>
<html lang="en">
<head>
<meta charset="utf-8">
<title>Lorne Patek Professional Corporation – Business Card</title>
<link rel="stylesheet" href="https://fonts.googleapis.com/css2?family=Cinzel:wght@500&family=Arimo:wght@400&display=swap">
<style>
  :root {
    --page-bg: #e9e7e3;
    --card-white: #ffffff;
    --ink-blue: #2e3192;
    --band-black: #050508;
    --accent-blue: #2e3192;
    --brand-blue: #3a3fb0;
    --muted-gray: #9a9aa0;
  }
  * { margin: 0; padding: 0; box-sizing: border-box; }
  html, body {
    width: 1200px; height: 800px; overflow: hidden;
    background: var(--page-bg);
  }
  .canvas {
    width: 1200px; height: 800px;
    display: flex; align-items: center; justify-content: center;
  }
  .card {
    position: relative;
    width: 1050px; height: 600px;
    background: var(--card-white);
    box-shadow: 0 10px 30px rgba(0,0,0,0.18);
    overflow: hidden;
  }
  .card-shapes { position: absolute; inset: 0; }
  .identity { position: absolute; left: 70px; top: 60px; color: var(--ink-blue); }
  .identity-name {
    font-family: "Cinzel", serif; font-weight: 500;
    font-size: 44px; letter-spacing: 1px; line-height: 1;
  }
  .identity-title {
    font-family: "Cinzel", serif; font-weight: 500;
    font-size: 22px; margin-top: 6px;
  }
  .contact-list {
    position: absolute; left: 70px; top: 195px;
    list-style: none; color: var(--ink-blue);
    font-family: "Arimo", sans-serif; font-size: 24px;
  }
  .contact-item { display: flex; align-items: flex-start; margin-bottom: 14px; }
  .contact-icon { width: 26px; height: 26px; margin-right: 22px; flex: none; fill: var(--ink-blue); }
  .contact-text { line-height: 1.2; }
  .brand {
    position: absolute; right: 60px; bottom: 70px;
    display: flex; align-items: center;
  }
  .brand-mark {
    width: 78px; height: 78px; border-radius: 50%;
    background: var(--brand-blue); margin-right: 20px; flex: none;
  }
  .brand-name {
    font-family: "Cinzel", serif; font-weight: 500;
    font-size: 40px; color: var(--brand-blue); line-height: 1;
  }
  .brand-sub {
    font-family: "Cinzel", serif; font-weight: 500;
    font-size: 15px; color: var(--brand-blue); letter-spacing: 1px; margin-top: 4px;
  }
  .brand-credentials {
    font-family: "Cinzel", serif; font-weight: 500;
    font-size: 13px; color: var(--muted-gray); letter-spacing: 1px; line-height: 1.3;
  }
</style>
</head>
<body>
<main class="canvas">
  <section class="card">
    <svg class="card-shapes" width="1050" height="600" viewBox="0 0 1050 600" aria-hidden="true">
      <polygon class="accent-stripe" points="200,600 1050,150 1050,172 330,600" fill="var(--accent-blue)"/>
      <polygon class="corner-band" points="330,600 1050,172 1050,600" fill="var(--band-black)"/>
    </svg>

    <header class="identity">
      <h1 class="identity-name">Lorne Patek</h1>
      <p class="identity-title">CPA, CGA</p>
    </header>

    <ul class="contact-list">
      <li class="contact-item">
        <svg class="contact-icon" viewBox="0 0 24 24"><path d="M6.6 10.8a15.1 15.1 0 0 0 6.6 6.6l2.2-2.2a1 1 0 0 1 1-.25 11.4 11.4 0 0 0 3.6.57 1 1 0 0 1 1 1V20a1 1 0 0 1-1 1A17 17 0 0 1 3 4a1 1 0 0 1 1-1h3.5a1 1 0 0 1 1 1c0 1.25.2 2.45.57 3.6a1 1 0 0 1-.25 1z"/></svg>
        <span class="contact-text">(416) 555-0142</span>
      </li>
      <li class="contact-item">
        <svg class="contact-icon" viewBox="0 0 24 24"><path d="M6.6 10.8a15.1 15.1 0 0 0 6.6 6.6l2.2-2.2a1 1 0 0 1 1-.25 11.4 11.4 0 0 0 3.6.57 1 1 0 0 1 1 1V20a1 1 0 0 1-1 1A17 17 0 0 1 3 4a1 1 0 0 1 1-1h3.5a1 1 0 0 1 1 1c0 1.25.2 2.45.57 3.6a1 1 0 0 1-.25 1z"/></svg>
        <span class="contact-text">(416) 555-0187</span>
      </li>
      <li class="contact-item">
        <svg class="contact-icon" viewBox="0 0 24 24"><path d="M2 5h20v14H2z M3.5 6.5 12 13l8.5-6.5" fill="var(--ink-blue)" stroke="#fff" stroke-width="1.4"/></svg>
        <span class="contact-text">lorne@lornepatek.example</span>
      </li>
      <li class="contact-item">
        <svg class="contact-icon" viewBox="0 0 24 24"><path d="M12 2a7 7 0 0 0-7 7c0 5.2 7 13 7 13s7-7.8 7-13a7 7 0 0 0-7-7zm0 9.5a2.5 2.5 0 1 1 0-5 2.5 2.5 0 0 1 0 5z"/></svg>
        <span class="contact-text">47 Marrow Creek Rd. Elmbrook,<br>ON K7T 5P3</span>
      </li>
    </ul>

    <div class="brand">
      <span class="brand-mark"></span>
      <div class="brand-text">
        <p class="brand-name">LORNE PATEK</p>
        <p class="brand-sub">PROFESSIONAL CORPORATION</p>
        <p class="brand-credentials">CHARTERED PROFESSIONAL ACCOUNTANT<br>CERTIFIED GENERAL ACCOUNTANT</p>
      </div>
    </div>
  </section>
</main>
</body>
</html>
```